Kevmoor belly band - cardboard to wrap around a plain tin for Gift

We are packaging men's and ladies handkerchiefs into tins for Gifts. We need two belly band designs to wrap around a small tin which measures 140 x 100 x 43 depth. The band to measure approx 90 w x 330 long inclusive is 30mm lapover . The ladies design (white tin) to have a subtle floral background with the word .Kevmoor. only placed on front centre of tin. The men's (black tin) to have a masculine look with the logo .Kevmoor. (the word can be taken out of the oval logo. This to placed in centre on front of tin. Men's could have a tan or cream textured look??

Target Market(s)

30 to 80 year old market

Font styles to use
Other font styles liked:
• Mona lisa

Colors

Designer to choose colors to be used in the design.

Requirements
Must have
• Two different designs one for men's black tin and one for ladies white tin.
• Must have continuous design with logo in centre once wrapped around the tin.
• Both must have an upmarket classy look.
• Tins will be displayed horizontal.
Nice to have
• Ladies would like to see soft floral not too over the top feminine classy look.
• Mens more masculine and upmarket maybe plain with a textured look.
• A design has been attached - like this sort of look for ladies!

```html
<!DOCTYPE html>
<html lang="en">
<head>
<meta charset="utf-8">
<title>Kevmoor Handkerchief Belly Bands</title>
<link href="https://fonts.googleapis.com/css2?family=Playfair+Display:wght@400&family=Cormorant+Garamond:wght@500;600&family=Raleway:wght@300;400&display=swap" rel="stylesheet">
<style>
  :root {
    --page: #e4e4e4;
    --teal: #0f3b44;
    --teal-deep: #0b2f37;
    --blush: #dcbcbc;
    --mist: #d6dadb;
    --rule-light: rgba(214, 218, 219, 0.55);
    --cream: #dcd6cb;
    --cream-band: #cbc4b8;
    --charcoal: #3a3a3a;
    --rule-dark: rgba(58, 58, 58, 0.45);
    --gold: #c9a23f;
    --petal: #e7a9b4;
    --peony: #c7374d;
    --leaf: #6f8f4a;
  }
  * { margin: 0; padding: 0; box-sizing: border-box; }
  html, body { width: 1200px; height: 900px; overflow: hidden; background: var(--page); }
  .canvas { position: relative; width: 1200px; height: 900px; }

  .band { position: absolute; top: 252px; width: 494px; height: 454px; overflow: hidden; }
  .band--ladies { left: 44px; background: var(--teal); }
  .band--mens { left: 652px; background: var(--cream); }

  .floral { position: absolute; }
  .floral--top {
    left: 0; top: 0; width: 250px; height: 160px;
    background: radial-gradient(ellipse at 30% 40%, var(--petal) 0%, rgba(231,169,180,0.7) 28%, rgba(111,143,74,0.55) 50%, rgba(15,59,68,0) 72%);
  }
  .floral--bottom {
    right: 0; bottom: 0; width: 260px; height: 170px;
    background: radial-gradient(ellipse at 70% 70%, var(--peony) 0%, rgba(231,169,180,0.75) 30%, rgba(111,143,74,0.5) 52%, rgba(15,59,68,0) 74%);
  }

  .wordmark { position: absolute; overflow: visible; }
  .wordmark text { font-family: "Playfair Display", serif; font-weight: 400; }

  .tagline {
    position: absolute; font-family: "Cormorant Garamond", serif; font-weight: 600;
    text-transform: uppercase; white-space: nowrap; font-size: 13px; letter-spacing: 0.4px;
  }
  .rule { position: absolute; height: 1px; }
  .product {
    position: absolute; font-family: "Raleway", sans-serif; line-height: 1; white-space: nowrap;
  }
  .product__line { display: block; font-weight: 400; font-size: 23px; letter-spacing: -0.3px; }
  .product__name { display: block; font-weight: 300; font-size: 22px; margin-top: 3px; }
  .since { position: absolute; font-family: "Cormorant Garamond", serif; font-weight: 600; font-size: 19px; white-space: nowrap; }

  .band--ladies .tagline, .band--ladies .product, .band--ladies .since { color: var(--mist); }
  .band--ladies .rule { background: var(--rule-light); }

  .band--mens .tagline, .band--mens .product, .band--mens .since { color: var(--charcoal); }
  .band--mens .rule { background: var(--rule-dark); }
  .title-strip { position: absolute; left: 0; top: 92px; width: 100%; height: 164px; background: var(--cream-band); }
  .flourish {
    position: absolute; left: 136px; top: 260px; width: 222px; height: 32px;
    background: linear-gradient(90deg, rgba(201,162,63,0) 0%, var(--gold) 30%, var(--gold) 70%, rgba(201,162,63,0) 100%);
    clip-path: polygon(0 45%, 40% 20%, 50% 0, 60% 20%, 100% 45%, 100% 55%, 60% 80%, 50% 100%, 40% 80%, 0 55%);
  }
</style>
</head>
<body>
<div class="canvas">

  <section class="band band--ladies">
    <div class="floral floral--top" role="img" aria-label="Watercolour pink peony with buds and maidenhair fern leaves"></div>
    <div class="floral floral--bottom" role="img" aria-label="Watercolour red and cream peonies with fern leaves"></div>

    <svg class="wordmark" style="left:70px;top:130px" width="420" height="130" viewBox="0 0 420 130">
      <text x="4" y="112" font-size="138" fill="var(--blush)" textLength="344" lengthAdjust="spacingAndGlyphs">Kevmoor</text>
      <text x="362" y="38" font-size="20" fill="var(--mist)" font-family="Raleway, sans-serif">®</text>
    </svg>
    <div class="rule" style="left:74px;top:258px;width:344px"></div>
    <p class="tagline" style="left:74px;top:268px">Organic Cotton · 100% Natural · Premium Febric</p>

    <div class="rule" style="left:74px;top:312px;width:104px"></div>
    <p class="product" style="left:74px;top:328px">
      <span class="product__line">DES IGNER</span>
      <span class="product__name">Handkerchiefs</span>
    </p>
    <div class="rule" style="left:74px;top:390px;width:158px"></div>
    <p class="since" style="left:74px;top:397px">Since 1918</p>
  </section>

  <section class="band band--mens">
    <div class="title-strip"></div>

    <svg class="wordmark" style="left:70px;top:96px" width="420" height="130" viewBox="0 0 420 130">
      <text x="4" y="112" font-size="138" fill="var(--charcoal)" textLength="344" lengthAdjust="spacingAndGlyphs">Kevmoor</text>
      <text x="356" y="32" font-size="20" fill="var(--charcoal)" font-family="Raleway, sans-serif">®</text>
    </svg>
    <div class="rule" style="left:74px;top:222px;width:344px"></div>
    <p class="tagline" style="left:94px;top:230px">Organic Cotton · 100% Natural · Premium Febric</p>

    <div class="flourish" role="img" aria-label="Gold ornamental scroll divider"></div>

    <p class="product" style="left:0;width:494px;top:318px;text-align:center">
      <span class="product__line">DES IGNER</span>
      <span class="product__name">Handkerchiefs</span>
    </p>
    <div class="rule" style="left:168px;top:380px;width:158px"></div>
    <p class="since" style="left:0;width:494px;top:386px;text-align:center">Since 1918</p>
  </section>

</div>
</body>
</html>
```